International business needs a web page design

We need a web page design for a new service that our new "sub-company" of our existing company will offer. We are based in Denmark, and our new "sub-company" is called 'Velkari'. The service we offer is automated server configuration and In-Depth monitoring, and optional operations support. Our monitoring has a lot of graphs (like those seen here: https://velkari.example/ with either black or white background ) and the website needs to communicate a sense of Security/safety and that our customers can relax, because we have the full overview of their service and servers. The website should not be with black background.

We deliver low price, high quality and professional operations - which we can do, because we automate it and have people with 15+ years of experience doing so.

We have attached :
a file with our logo : velkari
a file showing the content of the frontage : frontpage
a file showing the content of the user page(for logged in users) : User page
a file showing the pop-up dialog "page" : CallToAction_route
a file showing the 3-steps for the frontpage : 3-step for frontpage

Target Market(s)

Chief Technological officers (CTO's) and Developers (small business, run by developers) - who needs professional IT operations.

Industry/Entity Type

Business

Coding

Coded - Design and coding required

Number of Pages Required

3 page

Requirements
Must have
• Frontpage :
• A lot of visualization(some with people too) rather than a lot of text
• A short, describing text on front page telling what people get
• 3 steps showing people how it works. (Could be presented in a video placed on top of a big front image or perhaps with all 3 steps/pictures shown at the same time or perhaps in a completely different way).
Nice to have
• A big front image(perhaps a person with a cellphone showing graphs and a "all okay" message) with a text and the 3-steps pictures/or video on top of it
• 3 boxes under the front image/top of the site showing what benefits people get from the service
Should not have
• Not a black/dark site

```html
<!DOCTYPE html>
<html lang="en">
<head>
<meta charset="utf-8">
<title>Velkari – Instant server setup & in-depth monitoring</title>
<link rel="stylesheet" href="https://fonts.googleapis.com/css2?family=Open+Sans:ital,wght@0,400;0,600;0,700;1,400&family=Ubuntu:wght@400;500&family=Roboto:wght@400;700&display=swap">
<style>
  :root{
    --brand:#0ba0d9;
    --brand-dark:#0f6a8e;
    --ink:#1d1d1d;
    --heading:#3a3a3a;
    --muted:#8a8a8a;
    --soft-bg:#f7f7f7;
    --footer:#323232;
    --footer-bottom:#262626;
    --white:#ffffff;
  }
  *{box-sizing:border-box;margin:0;padding:0}
  html,body{width:724px;height:1200px;overflow:hidden;background:var(--white)}
  body{position:relative;font-family:"Open Sans",Arial,sans-serif;color:var(--ink)}
  .abs{position:absolute}

  /* header */
  .site-header{position:absolute;left:0;top:0;width:724px;height:50px;background:var(--white)}
  .brand{position:absolute;left:68px;top:9px;display:flex;align-items:center;gap:7px}
  .brand-dot{width:32px;height:32px;border-radius:50%;background:var(--brand)}
  .brand-name{font-family:"Ubuntu",sans-serif;font-weight:500;font-size:24px;color:#222;letter-spacing:-.3px}
  .top-links{position:absolute;right:124px;top:19px;display:flex;gap:14px;font-size:8.6px;color:#7a7a7a}
  .like-badge{position:absolute;left:616px;top:20px;width:42px;height:11px;border-radius:2px;background:#3b5998}

  .main-nav{position:absolute;left:0;top:50px;width:724px;height:34px;background:var(--brand)}
  .main-nav a{position:absolute;top:0;height:34px;line-height:34px;font-size:9.6px;font-weight:700;color:var(--white);text-decoration:none}
  .main-nav a.active{left:66px;width:58px;text-align:center;background:var(--brand-dark)}

  /* hero */
  .hero{position:absolute;left:0;top:84px;width:724px;height:316px;overflow:hidden}
  .hero-photo{position:absolute;inset:0;background:linear-gradient(90deg,#eceae6 0%,#d9d7d2 45%,#a9b0b8 68%,#7f8fa9 82%,#c9c6c0 100%)}
  .hero-title{position:absolute;left:68px;top:63px;font-family:"Roboto",sans-serif;font-size:29.5px;line-height:31px;font-weight:400;color:#111}
  .hero-title b{font-weight:700}
  .hero-text{position:absolute;left:68px;top:134px;width:285px;font-size:9.4px;line-height:13.4px;color:#1a1a1a}
  .btn-primary{position:absolute;left:68px;top:204px;width:100px;height:30px;line-height:29px;text-align:center;background:var(--brand);color:var(--white);font-size:10.5px;border-bottom:2px solid #0a7fad;border-radius:2px}
  .slider-dots{position:absolute;left:350px;top:291px;display:flex;gap:3px}
  .slider-dots span{width:6px;height:6px;border-radius:50%;background:var(--white)}
  .slider-dots span.on{background:var(--brand)}

  /* sections */
  .section-title{position:absolute;left:0;width:724px;text-align:center;font-family:"Ubuntu",sans-serif;font-weight:500;font-size:17.5px;color:var(--heading)}
  .section-sub{position:absolute;left:0;width:724px;text-align:center;font-style:italic;font-size:10.4px;color:var(--muted)}

  .video-thumb{position:absolute;left:80px;top:510px;width:297px;height:168px;background:linear-gradient(160deg,#2c3e57 0%,#3e5675 55%,#6e82a4 100%)}
  .play{position:absolute;left:128px;top:63px;width:42px;height:42px}
  .how-title{position:absolute;left:410px;top:520px;font-family:"Ubuntu",sans-serif;font-size:16px;color:#444}
  .how-text{position:absolute;left:410px;width:250px;font-size:9px;line-height:15px;color:#8a8a8a}
  .btn-small{position:absolute;left:410px;top:646px;width:78px;height:20px;line-height:20px;text-align:center;background:var(--brand);color:var(--white);font-size:8.6px;font-weight:700;border-radius:1px}

  .services{position:absolute;left:0;top:710px;width:724px;height:348px;background:var(--soft-bg)}
  .service{position:absolute;top:108px;width:180px;text-align:center}
  .service-icon{display:block;margin:0 auto;width:96px;height:96px}
  .service-title{margin-top:17px;font-family:"Ubuntu",sans-serif;font-size:12.6px;line-height:14.6px;color:#333}
  .service-text{margin-top:11px;font-size:9px;line-height:15px;color:#8e8e8e}
  .service-link{margin-top:9px;font-size:9px;font-weight:600;color:var(--brand)}

  /* footer */
  .site-footer{position:absolute;left:0;top:1058px;width:724px;height:110px;background:var(--footer);color:var(--white)}
  .footer-brand{position:absolute;left:68px;top:18px;display:flex;align-items:center;gap:6px}
  .footer-brand .brand-dot{width:28px;height:28px}
  .footer-brand .brand-name{color:var(--white);font-size:21px}
  .footer-about{position:absolute;left:68px;top:63px;width:150px;font-family:Arial,sans-serif;font-weight:700;font-size:7.8px;line-height:12.4px}
  .footer-list{position:absolute;list-style:none;font-family:Arial,sans-serif;font-size:7.8px;line-height:12px}
  .newsletter-text{position:absolute;left:470px;top:18px;width:190px;font-family:"Ubuntu",sans-serif;font-size:8.4px;line-height:10.6px}
  .newsletter{position:absolute;left:469px;top:55px;width:189px;height:24px;background:var(--white);border:1px solid #ddd}
  .newsletter span{position:absolute;left:8px;top:6px;font-family:Arial,sans-serif;font-style:italic;font-size:7.8px;color:#222}
  .newsletter b{position:absolute;right:2px;top:2px;width:60px;height:18px;line-height:18px;text-align:center;background:var(--brand);font-family:Arial,sans-serif;font-size:8px;color:var(--white)}

  .footer-bottom{position:absolute;left:0;top:1168px;width:724px;height:32px;background:var(--footer-bottom)}
  .copyright{position:absolute;left:68px;top:11px;font-size:7.4px;color:var(--white)}
  .social{position:absolute;top:8px;width:16px;height:16px;border-radius:50%;background:var(--white)}
</style>
</head>
<body>

<header class="site-header">
  <div class="brand"><span class="brand-dot"></span><span class="brand-name">Velkari</span></div>
  <nav class="top-links"><span>Company</span><span>In the Press</span><span>Event</span><span>Resources</span><span>Blog</span></nav>
  <span class="like-badge"></span>
</header>

<nav class="main-nav">
  <a class="active">Home</a>
  <a style="left:134px">Why Choose Us</a>
  <a style="left:227px">About Us</a>
  <a style="left:294px">Services</a>
  <a style="left:358px">Contact Us</a>
</nav>

<section class="hero">
  <div class="hero-photo" role="img" aria-label="Photo of a bearded businessman in a waistcoat talking on his phone on a city street"></div>
  <h1 class="hero-title">Instant server <b>Setup</b> &amp;<br>in-Depth <b>Monitoring</b></h1>
  <p class="hero-text">Lorem ipsum dolor sit amet is consectetur adipiscing elit sed do eiusmod the tempor incididunt labore et dolore the magna aliqua eim minim veniam quis nostrud exercitation ullamco laboris nisi ut aliquip the commodo consiequat duis aute irure dolor in</p>
  <a class="btn-primary">TRY IT FOR FREE</a>
  <div class="slider-dots"><span class="on"></span><span></span><span></span></div>
</section>

<h2 class="section-title" style="top:433px">OUR VIDEO</h2>
<p class="section-sub" style="top:463px">Lorem ipsum dolor sit amet consectetur adipiscing elit sed do eiusmod tempor incididunt .</p>

<div class="video-thumb" role="img" aria-label="Video still of stock market charts over a world map">
  <svg class="play" viewBox="0 0 42 42"><circle cx="21" cy="21" r="19" fill="#fff"/><circle cx="21" cy="21" r="16" fill="#111"/><path d="M16 12 L30 21 L16 30 Z" fill="#fff"/></svg>
</div>
<h3 class="how-title">How we do it</h3>
<p class="how-text" style="top:545px">Lorem ipsum dolor sit amiet is consectetur adipiscing elit sed do eiusmod tempor incididuint labore dolore magna aliqua enim ad minim veniam.</p>
<p class="how-text" style="top:597px">quis nostrud exercitation ullamco laboris nisi ut aliquip ex ea commodo consequat.</p>
<a class="btn-small">Read More</a>

<section class="services">
  <h2 class="section-title" style="top:32px">OUR SERVICES</h2>
  <p class="section-sub" style="top:63px">Lorem ipsum dolor sit amet consectetur adipiscing elit sed do eiusmod tempor incididunt .</p>

  <div class="service" style="left:92px">
    <svg class="service-icon" viewBox="0 0 96 96"><circle cx="48" cy="48" r="48" fill="var(--brand)"/>
      <circle cx="48" cy="38" r="11" fill="#fff"/>
      <path d="M27 68 Q27 53 40 51 L48 58 L56 51 Q69 53 69 68 Z" fill="#fff"/>
      <path d="M46 55 L50 55 L51 66 L48 68 L45 66 Z" fill="var(--brand)"/></svg>
    <div class="service-title">It’s Fast and Easy</div>
    <div class="service-text">Lorem ipsum dolor sit amiet is<br>consectetur adipiscing elit, sed<br>do eiusmod tempor.</div>
    <div class="service-link">Read More</div>
  </div>

  <div class="service" style="left:272px">
    <svg class="service-icon" viewBox="0 0 96 96"><circle cx="48" cy="48" r="48" fill="var(--brand)"/>
      <circle cx="36" cy="40" r="8" fill="#fff"/><circle cx="60" cy="40" r="8" fill="#fff"/>
      <path d="M21 64 Q21 52 36 51 Q51 52 51 64 Z" fill="#fff"/><path d="M45 64 Q45 52 60 51 Q75 52 75 64 Z" fill="#fff"/>
      <circle cx="48" cy="36" r="9.5" fill="#fff" stroke="var(--brand)" stroke-width="2"/>
      <path d="M31 67 Q31 51 48 49 Q65 51 65 67 Z" fill="#fff" stroke="var(--brand)" stroke-width="2"/></svg>
    <div class="service-title">Relax and Rest Assured</div>
    <div class="service-text">Lorem ipsum dolor sit amiet is<br>consectetur adipiscing elit, sed<br>do eiusmod tempor.</div>
    <div class="service-link">Read More</div>
  </div>

  <div class="service" style="left:452px">
    <svg class="service-icon" viewBox="0 0 96 96"><circle cx="48" cy="48" r="48" fill="var(--brand)"/>
      <rect x="28" y="30" width="40" height="36" rx="2" fill="none" stroke="#fff" stroke-width="3"/>
      <rect x="34" y="36" width="28" height="7" fill="#fff"/>
      <rect x="34" y="47" width="12" height="12" fill="#fff"/>
      <rect x="50" y="47" width="12" height="2.5" fill="#fff"/><rect x="50" y="52" width="12" height="2.5" fill="#fff"/><rect x="50" y="57" width="12" height="2.5" fill="#fff"/>
      <path d="M28 40 H24 V64 Q24 66 26 66" fill="none" stroke="#fff" stroke-width="3"/></svg>
    <div class="service-title">You’ll Love your Detailed<br>Performance Graphs</div>
    <div class="service-text">Lorem ipsum dolor sit amiet is<br>consectetur adipiscing elit, sed<br>do eiusmod tempor.</div>
    <div class="service-link">Read More</div>
  </div>
</section>

<footer class="site-footer">
  <div class="footer-brand"><span class="brand-dot"></span><span class="brand-name">Velkari</span></div>
  <p class="footer-about">Lorem ipsum dolor consectetur elit sed tempor incididunt labore dolore magna aliqua enim ad minim veniam.</p>
  <ul class="footer-list" style="left:254px;top:18px">
    <li>Home</li><li>Why Choose Us</li><li>About Us</li><li>Services</li><li>Contact Us</li>
  </ul>
  <ul class="footer-list" style="left:349px;top:18px;line-height:10px">
    <li>It’s Fast and Easy</li>
    <li style="margin-top:6px">Relax and Rest Assured</li>
    <li style="margin-top:6px">You’ll Love your Detailed<br>Performance Graphs</li>
  </ul>
  <p class="newsletter-text">Sign up to our newsletters to receive occasional e-mail updates about new features and offers.</p>
  <div class="newsletter"><span>Enter Your Email</span><b>SUBSCRIBE</b></div>
</footer>

<div class="footer-bottom">
  <p class="copyright">Copyrights © 2014. Velkari . All Rights Reserved</p>
  <span class="social" style="left:604px"></span>
  <span class="social" style="left:623px"></span>
  <span class="social" style="left:642px"></span>
</div>

</body>
</html>
```